Harrowden Metal recycling, a business card/logo for our industrial family metal recycling company

A new business card design/logo for our long established family metal recycling company.
I have a logo for our property company which was designed a few months ago on pixel forge which I would like to be very close to this design but have a more industrial feel to it and in a darker blue colour, please see attachments.

Target Market(s)

industries that produce metal waste for recycling, construction sites, engineering companies, manufactures, builders, plumbers, electricians, general house holders.

Industry/Entity Type

Recycling

Contact Information for Business Card

owner/director...Martin harrowden
e-mail....info@harrowdenscrapworks.co.uk
web address.....harrowdenscrapworks.co.uk

Font styles to use
Serif
Sans Serif

Colors
0255a3
ffffff

Requirements
Must have
• -dark blue business card on front.
-white on the back, see contact details, e-mail address for metal company.
-to have an industrial feel to it.
-harrowden logo as business card attached but (harrowden metal recycling)
please remove the little roof/arrow above harrowden as this was relevant to property company.
Nice to have
• please see our website harrowdenscrapworks.co.uk with all details
being correct however I would like to refresh the logo to more like the harrowden property investment business card logo attached.
Should not have
• should not contain details from property investments card as this design is for the metal recycling company.

```html
<!DOCTYPE html>
<html lang="en">
<head>
<meta charset="utf-8">
<title>Harrowden Metal Recycling — Business Card</title>
<link rel="stylesheet" href="https://fonts.googleapis.com/css2?family=Raleway:wght@300;400;700&display=swap">
<style>
  :root {
    --canvas: #a9aaac;
    --card-navy: #021a28;
    --blob-black: #02090f;
    --edge-line: #04202f;
    --ink-white: #ffffff;
    --ink-soft: #eef1f4;
  }
  html, body {
    margin: 0;
    padding: 0;
    width: 1200px;
    height: 1200px;
    overflow: hidden;
    background: var(--canvas);
  }
  .sheet {
    position: relative;
    width: 1200px;
    height: 1200px;
  }
  .card {
    position: absolute;
    left: 285px;
    width: 630px;
    height: 360px;
    display: block;
  }
  .card--front { top: 150px; }
  .card--back  { top: 604px; }

  .card__base  { fill: var(--card-navy); }
  .card__blob  { fill: var(--blob-black); }
  .card__edge  { fill: none; stroke: var(--edge-line); stroke-width: 3; }

  .brand-name {
    font-family: "Raleway", sans-serif;
    font-weight: 300;
    fill: var(--ink-white);
    text-anchor: middle;
  }
  .brand-tagline {
    font-family: "Raleway", sans-serif;
    font-weight: 400;
    fill: var(--ink-soft);
    text-anchor: middle;
  }
  .person-name {
    font-family: "Raleway", sans-serif;
    font-weight: 700;
    font-size: 20px;
    letter-spacing: 1.2px;
    fill: var(--ink-white);
    text-anchor: middle;
  }
  .person-role {
    font-family: "Raleway", sans-serif;
    font-weight: 400;
    font-size: 15px;
    letter-spacing: 1px;
    fill: var(--ink-white);
    text-anchor: middle;
  }
  .contact-line {
    font-family: "Raleway", sans-serif;
    font-weight: 400;
    font-size: 16px;
    letter-spacing: 0.8px;
    fill: var(--ink-white);
    text-anchor: middle;
  }
  .divider-square { fill: var(--ink-white); }
</style>
</head>
<body>
<main class="sheet">

  <svg class="card card--front" viewBox="0 0 630 360" aria-label="Business card front">
    <rect class="card__base" width="630" height="360"/>
    <path class="card__edge" d="M160,0 C80,90 12,170 14,232 C16,290 60,330 118,360"/>
    <path class="card__edge" d="M522,0 C600,70 625,140 608,205 C592,270 548,320 516,360"/>
    <path class="card__blob" d="M173,0 L518,0 C595,78 608,148 592,210 C574,276 534,318 505,360 L128,360 C66,322 32,284 34,232 C36,172 96,92 173,0 Z"/>

    <text class="brand-name" x="314" y="117" font-size="58" letter-spacing="2">harrowden</text>
    <text class="brand-tagline" x="314" y="135" font-size="11" letter-spacing="10">METAL RECYCLING</text>

    <text class="person-name" x="314" y="237">Martin Harrowden</text>
    <text class="person-role" x="314" y="259">Owner-Director</text>
    <rect class="divider-square" x="297" y="271" width="12" height="12"/>
    <rect class="divider-square" x="321" y="271" width="12" height="12"/>
    <text class="contact-line" x="314" y="307">info@harrowdenscrapworks.co.uk</text>
    <text class="contact-line" x="314" y="329">harrowdenscrapworks.co.uk</text>
  </svg>

  <svg class="card card--back" viewBox="0 0 630 360" aria-label="Business card back">
    <rect class="card__base" width="630" height="360"/>
    <path class="card__edge" d="M185,0 C110,90 28,190 28,258 C28,310 70,345 98,360"/>
    <path class="card__edge" d="M555,0 C610,60 626,130 610,195 C592,262 520,320 472,360"/>
    <path class="card__blob" d="M191,0 L548,0 C600,66 610,130 594,192 C574,262 500,318 451,360 L106,360 C64,330 48,300 48,259 C48,196 120,96 191,0 Z"/>

    <text class="brand-name" x="315" y="200" font-size="80" letter-spacing="3">harrowden</text>
    <text class="brand-tagline" x="315" y="232" font-size="14" letter-spacing="13">METAL RECYCLING</text>
  </svg>

</main>
</body>
</html>
```